Broschüren für Kinderteppich Kollektion
Zielgruppe
TAMURO.DE aus Herxheim in der Pfalz will Spiel und Spaß im Kinderzimmer: Wir bieten Ihnen hochwertige und kreative Teppiche für Kinder und Jugendliche, sowie farbenfrohe und trendige Spielteppiche.
Aufgabenstellung
Wir planen einen Broschüre für unsere Kollektion ' Pebble line' handgemachte Kinderteppiche aus Wolle und Baumwolle. B2B Bereich.
Wenig Text..große Bilder und alles in sehr schlichtem Design.
Das Druckmass sollte DIN A5 oder quadratisch sein.
Umfang ca. 15-20 Designs in verschiedenen Farbkombinationen. Teppiche werden im Plattschuss gezeigt..und ergänzt durch Nahaufnahmen der Struktur.
Wir sind nun in der Planung soweit, das wir die Broschüre quadratisch machen, wie auch die meisten bevorzugen.
Seitenanzahl wird mit Umschlag 20 Seiten sein.Designanzahl nun exact:
1) Wolle handmade: : Swirlmix in drei Farben, Moonkite in drei Farben, und neue Designs: Design: WAVE: in 8 Farben und design BLOOM in drei Farben:
Insgesamt Wolle 17 Farbstellungen und das jeweils in drei Größen.
2) Baumwolle : Maple in drei Farben und zwei Größen.
Fotos sind alle Hochauflösend vorhanden. ( NEUE Kollektion WAVE und BLOOM sind gerade beim fotographieren)

```html
<!DOCTYPE html>
<html lang="de">
<head>
<meta charset="utf-8">
<title>Pebble line – Kinderteppiche</title>
<link href="https://fonts.googleapis.com/css2?family=Cabin:wght@400;500&family=Gochi+Hand&display=swap" rel="stylesheet">
<style>
  :root{
    --backdrop:#c3aabb;
    --paper:#ffffff;
    --paper-right:#f7f7f7;
    --orange:#e8843a;
    --lilac:#c47aa6;
    --band:#ebebea;
    --band-head:#dcdad8;
    --rule:#ffffff;
    --text:#8d8d8d;
    --text-dark:#6f6f6f;
    --photo-lilac:#c9b6c6;
    --photo-grey:#a9aeb3;
    --photo-cream:#ddd8cf;
    --photo-stars:#d8d5cf;
  }
  *{box-sizing:border-box;margin:0;padding:0}
  html,body{width:1200px;height:800px;overflow:hidden}
  body{background:var(--backdrop);font-family:"Cabin",sans-serif;color:var(--text);position:relative}
  .spread{position:absolute;left:60px;top:120px;width:1080px;height:560px;display:flex}
  .page{position:relative;width:540px;height:560px;background:var(--paper)}
  .page--right{background:var(--paper-right)}

  .photo{position:absolute}
  .photo--lilac-fold{left:27px;top:21px;width:317px;height:264px;background:linear-gradient(160deg,#d3c2d1 0%,var(--photo-lilac) 55%,#a897a6 100%)}
  .photo--grey-dots{left:354px;top:21px;width:152px;height:127px;background:linear-gradient(170deg,#b9bdc1,var(--photo-grey))}
  .photo--star-detail{left:353px;top:157px;width:152px;height:130px;background:linear-gradient(160deg,#e4e0d9,#bfc0c0)}
  .photo--cream-fold{left:25px;top:294px;width:158px;height:242px;background:linear-gradient(150deg,var(--photo-cream),#bfb7aa)}
  .photo--blue-stars{left:191px;top:296px;width:314px;height:244px;background:linear-gradient(165deg,var(--photo-stars),#c4c0ba)}

  .brand{position:absolute;left:27px;top:25px;width:93px;height:90px;background:var(--paper);display:flex;align-items:center;justify-content:center;gap:5px}
  .brand__dot{width:10px;height:10px;background:var(--orange)}
  .brand__name{font-family:"Cabin",sans-serif;font-weight:500;font-size:16px;color:var(--orange);letter-spacing:.5px}

  .overview__title{position:absolute;left:37px;top:80px;font-family:"Gochi Hand",cursive;font-weight:400;font-size:22px;color:var(--orange);letter-spacing:.5px}
  .overview__subtitle{position:absolute;left:37px;top:107px;font-size:12px;color:var(--text-dark)}

  .legend{position:absolute;top:81px;display:flex;flex-direction:column;align-items:center;width:50px}
  .legend--wool{left:422px}
  .legend--cotton{left:477px}
  .legend__label{font-size:8px;margin-top:4px;color:var(--text)}

  .mat{display:inline-block;border-radius:50%;position:relative}
  .mat--big{width:26px;height:26px}
  .mat--small{width:11px;height:11px}
  .mat--wool{background:var(--orange)}
  .mat--cotton{background:var(--lilac)}
  .mat--big.mat--wool,.mat--big.mat--cotton{opacity:.75}
  .mat::after{content:"";position:absolute;left:28%;top:28%;width:44%;height:36%;border:1px solid #fff;border-radius:45% 45% 40% 40%}

  .price-table{position:absolute;left:37px;top:137px;width:489px}
  .price-table__head,.price-table__row{display:grid;grid-template-columns:42px 74px 89px 1fr 80px;align-items:center;padding:0 9px}
  .price-table__head{height:21px;background:var(--band-head);font-size:8.5px;color:var(--text-dark);font-weight:500}
  .price-table__head .price-table__label--model{grid-column:1 / 3}
  .price-table__group{background:var(--band);margin-top:8px}
  .price-table__row{height:23px;font-size:8px;border-top:1px solid var(--rule);white-space:nowrap}
  .price-table__row:first-child{border-top:none}
  .price-table__icons{display:flex;gap:4px}
  .price-table__model{font-size:9px}
  .price-table__price{text-align:right}

  .footnote{position:absolute;left:37px;top:517px;width:420px;font-size:6.5px;line-height:1.5;color:var(--text)}
  .folio{position:absolute;left:496px;top:517px;width:30px;height:37px;background:var(--orange);color:#fff;font-size:7px;text-align:center;padding-top:6px}
  .folio::after{content:"";display:block;width:20px;height:1px;background:#fff;margin:6px auto 0}
</style>
</head>
<body>
<div class="spread">
  <section class="page page--left">
    <div class="photo photo--lilac-fold" role="img" aria-label="Nahaufnahme eines fliederfarbenen Teppichs mit grauem Punkt und umgeschlagener Kante"></div>
    <div class="photo photo--grey-dots" role="img" aria-label="Grauer Teppich mit pastellfarbenen Punkten"></div>
    <div class="photo photo--star-detail" role="img" aria-label="Naturweißer Teppich mit grauen Sternen"></div>
    <div class="photo photo--cream-fold" role="img" aria-label="Umgeschlagene Kante eines naturfarbenen Teppichs mit mintfarbenem Punkt"></div>
    <div class="photo photo--blue-stars" role="img" aria-label="Naturweißer Teppich mit blauen und grauen Sternen"></div>
    <div class="brand"><span class="brand__dot"></span><span class="brand__name">TAMURO</span></div>
  </section>

  <section class="page page--right">
    <h1 class="overview__title">Pebble line</h1>
    <p class="overview__subtitle">Unsere Kinderteppiche in der Übersicht</p>

    <div class="legend legend--wool"><span class="mat mat--big mat--wool"></span><span class="legend__label">Schurwolle</span></div>
    <div class="legend legend--cotton"><span class="mat mat--big mat--cotton"></span><span class="legend__label">Baumwolle</span></div>

    <div class="price-table">
      <div class="price-table__head"><span class="price-table__label--model">Modell</span><span>Maße</span><span>Farbvarianten</span><span class="price-table__price">Netto in EUR</span></div>

      <div class="price-table__group">
        <div class="price-table__row"><span class="price-table__icons"><i class="mat mat--small mat--wool"></i></span><span class="price-table__model">Swirlmix</span><span>100 x 160 cm</span><span>flieder/multi, grau/multi, natur/multi</span><span class="price-table__price">190.00,- €</span></div>
        <div class="price-table__row"><span class="price-table__icons"><i class="mat mat--small mat--wool"></i></span><span class="price-table__model">Swirlmix</span><span>120 x 180 cm</span><span>flieder/multi, grau/multi, natur/multi</span><span class="price-table__price">220.00,- €</span></div>
        <div class="price-table__row"><span class="price-table__icons"><i class="mat mat--small mat--wool"></i></span><span class="price-table__model">Swirlmix</span><span>160 x 230 cm</span><span>flieder/multi, grau/multi, natur/multi</span><span class="price-table__price">280.00,- €</span></div>
      </div>

      <div class="price-table__group">
        <div class="price-table__row"><span class="price-table__icons"><i class="mat mat--small mat--wool"></i></span><span class="price-table__model">Moonkite</span><span>100 x 160 cm</span><span>natur/blau-grau, natur/grau, natur/rosa-rot</span><span class="price-table__price">190.00,- €</span></div>
        <div class="price-table__row"><span class="price-table__icons"><i class="mat mat--small mat--wool"></i></span><span class="price-table__model">Moonkite</span><span>120 x 180 cm</span><span>natur/blau-grau, natur/grau, natur/rosa-rot</span><span class="price-table__price">220.00,- €</span></div>
      </div>

      <div class="price-table__group">
        <div class="price-table__row"><span class="price-table__icons"><i class="mat mat--small mat--wool"></i><i class="mat mat--small mat--cotton"></i></span><span class="price-table__model">Wave</span><span>100 x 160 cm</span><span>flieder, blau, grau, rot, grün, natur, lila, rosa</span><span class="price-table__price">ab 190.00,- €</span></div>
        <div class="price-table__row"><span class="price-table__icons"><i class="mat mat--small mat--wool"></i><i class="mat mat--small mat--cotton"></i></span><span class="price-table__model">Wave</span><span>120 x 180 cm</span><span>flieder, blau, grau, rot, grün, natur, lila, rosa</span><span class="price-table__price">ab 220.00,- €</span></div>
        <div class="price-table__row"><span class="price-table__icons"><i class="mat mat--small mat--wool"></i><i class="mat mat--small mat--cotton"></i></span><span class="price-table__model">Wave</span><span>160 x 230 cm</span><span>flieder, blau, grau, rot, grün, natur, lila, rosa</span><span class="price-table__price">ab 280.00,- €</span></div>
      </div>

      <div class="price-table__group">
        <div class="price-table__row"><span class="price-table__icons"><i class="mat mat--small mat--wool"></i><i class="mat mat--small mat--cotton"></i></span><span class="price-table__model">Bloom</span><span>100 x 160 cm</span><span>flieder/multi, grau/multi, natur/multi</span><span class="price-table__price">ab 190.00,- €</span></div>
        <div class="price-table__row"><span class="price-table__icons"><i class="mat mat--small mat--wool"></i><i class="mat mat--small mat--cotton"></i></span><span class="price-table__model">Bloom</span><span>120 x 180 cm</span><span>flieder/multi, grau/multi, natur/multi</span><span class="price-table__price">ab 220.00,- €</span></div>
        <div class="price-table__row"><span class="price-table__icons"><i class="mat mat--small mat--wool"></i><i class="mat mat--small mat--cotton"></i></span><span class="price-table__model">Bloom</span><span>160 x 230 cm</span><span>flieder/multi, grau/multi, natur/multi</span><span class="price-table__price">ab 280.00,- €</span></div>
      </div>

      <div class="price-table__group">
        <div class="price-table__row"><span class="price-table__icons"><i class="mat mat--small mat--cotton"></i></span><span class="price-table__model">Maple</span><span>60 x 110 cm</span><span>blau, grau, rosa</span><span class="price-table__price">190.00,- €</span></div>
        <div class="price-table__row"><span class="price-table__icons"><i class="mat mat--small mat--cotton"></i></span><span class="price-table__model">Maple</span><span>90 x 160 cm</span><span>blau, grau, rosa</span><span class="price-table__price">220.00,- €</span></div>
      </div>
    </div>

    <p class="footnote">Ipidem uta aut quam nisque quasitiberit voluptur alignam unt maio. Et landi cuptistiis eicid quo. Alictus, officatur mos mil mosapedissi cume nimusam, sum seque molorpores explit estecae dolorer natemquunt.</p>
    <div class="folio">03</div>
  </section>
</div>
</body>
</html>
```